Lumora aesthetics offers a range of facial aesthetics treatments by a fully qualified dentist, to a high end crowd. Treatments include antiwrinkle treatment, the use of dermal fillers to provide facial volumisation and rejuvenation and also lip volumisation.
I want a luxurious and bold look. Black background with a bold striking gold logo in the centre possibly incorporating the outline of a face in a subtle yet effective way. I want it to include the work I offer so people will be aware of what they are looking into but not look like there's too much on the card, So it's a clean look.
At the bottom I would like it to say by Dr. Meera Sandhu. Alongside my email address and mobile number.

```html
<!DOCTYPE html>
<html lang="en">
<head>
<meta charset="UTF-8">
<title>Lumora Aesthetics – Business Card</title>
<link rel="stylesheet" href="https://fonts.googleapis.com/css2?family=Montserrat:wght@700;800&family=Open+Sans:wght@400;600;700&display=swap">
<style>
  :root {
    --backdrop: #161616;
    --card: #1d1d1d;
    --gold: #f2d63c;
    --gold-deep: #e6c21f;
    --band-light: #fff27a;
    --band-dark: #f0cc2a;
    --ink: #151515;
    --soft-text: #e9e9e9;
    --divider: #8a8a8a;
  }
  * { margin: 0; padding: 0; box-sizing: border-box; }
  html, body {
    width: 1200px;
    height: 1000px;
    overflow: hidden;
    background: var(--backdrop);
  }
  .canvas {
    position: relative;
    width: 1200px;
    height: 1000px;
    display: flex;
    align-items: center;
    justify-content: center;
  }
  .card {
    position: relative;
    width: 960px;
    height: 560px;
    background: var(--card);
    border-radius: 44px;
    overflow: hidden;
    box-shadow: 0 24px 60px rgba(0, 0, 0, 0.55);
  }
  .brand {
    position: absolute;
    top: 112px;
    left: 0;
    right: 0;
    display: flex;
    align-items: center;
    justify-content: center;
    gap: 22px;
  }
  .brand-name {
    font-family: "Montserrat", sans-serif;
    font-weight: 800;
    font-size: 64px;
    letter-spacing: 1px;
    color: var(--gold);
    text-transform: uppercase;
    line-height: 1;
  }
  .brand-mark {
    width: 26px;
    height: 26px;
    border-radius: 50%;
    background: var(--gold);
  }
  .details {
    position: absolute;
    top: 258px;
    left: 0;
    right: 0;
    display: flex;
    justify-content: center;
    align-items: center;
  }
  .doctor-name {
    font-family: "Open Sans", sans-serif;
    font-weight: 600;
    font-size: 38px;
    color: var(--gold);
    text-transform: uppercase;
    padding-right: 34px;
    white-space: nowrap;
  }
  .divider {
    width: 3px;
    height: 112px;
    background: var(--divider);
  }
  .contact {
    padding-left: 34px;
    font-family: "Open Sans", sans-serif;
    font-size: 19px;
    color: var(--soft-text);
    line-height: 1.3;
  }
  .contact-address { margin-bottom: 14px; }
  .contact-line {
    display: flex;
    align-items: center;
    gap: 14px;
  }
  .contact-line svg { width: 16px; height: 16px; flex: none; }
  .services-band {
    position: absolute;
    left: 0;
    right: 0;
    bottom: 0;
    height: 78px;
    background: linear-gradient(90deg, var(--band-dark), var(--band-light) 50%, var(--band-dark));
    display: flex;
    align-items: center;
    justify-content: center;
    gap: 18px;
    font-family: "Open Sans", sans-serif;
    font-weight: 700;
    font-size: 22px;
    letter-spacing: 0.5px;
    color: var(--ink);
    text-transform: uppercase;
  }
  .services-band .sep { font-weight: 400; }
</style>
</head>
<body>
<main class="canvas">
  <section class="card">
    <header class="brand">
      <h1 class="brand-name">Lumora Aesthetics</h1>
      <span class="brand-mark" aria-hidden="true"></span>
    </header>

    <div class="details">
      <p class="doctor-name">Dr. Meera Sandhu</p>
      <span class="divider" aria-hidden="true"></span>
      <address class="contact">
        <p class="contact-address">Your Street Address Here,<br>Country Name, 123</p>
        <p class="contact-line">
          <svg viewBox="0 0 16 16" aria-hidden="true"><path fill="#f2d63c" d="M3.5 1.5l2.2 2.6-1.3 1.6c.9 2 2.3 3.4 4.3 4.3l1.6-1.3 2.6 2.2-1.2 2.2c-5.2-.4-9.1-4.3-9.5-9.5z"/></svg>
          <span>+000 123 456 789</span>
        </p>
        <p class="contact-line">
          <svg viewBox="0 0 16 16" aria-hidden="true"><rect x="1" y="3.5" width="14" height="9.5" rx="1" fill="#f2d63c"/><path d="M1.5 4.2L8 9l6.5-4.8" fill="none" stroke="#1d1d1d" stroke-width="1.3"/></svg>
          <span>urname@email.com</span>
        </p>
      </address>
    </div>

    <footer class="services-band">
      <span>Facial Volumisation</span>
      <span class="sep">|</span>
      <span>Rejuvenation</span>
      <span class="sep">|</span>
      <span>Lip Volumisation</span>
    </footer>
  </section>
</main>
</body>
</html>
```